Legal firm website redesign

Existing site for Sydney CBD lawyer needs clean and professional redesign - http://brennicklaw.com.au

The site will be viewed by a wide range of users: businesses, individuals, referral partners and other lawyers.

Please see the list of must haves for further details

Target Market(s)

Businesses, individuals, referral partners and other lawyers

Industry/Entity Type

Lawyer

Requirements
Must have
• Prominent display of phone number.
List of services down the left hand side of the site (5x services or so).
Search box in header.
Please use the greys and blues from the existing header.
New header must include the wording "Efficiency - Fulfillment - Integrity - Teamwork"

```html
<!DOCTYPE html>
<html lang="en">
<head>
<meta charset="utf-8">
<title>Brennick Law – Commercial Lawyers Sydney</title>
<link href="https://fonts.googleapis.com/css2?family=Arimo:wght@400;700&display=swap" rel="stylesheet">
<style>
  :root {
    --nav-top: #8a8a8a;
    --nav-bottom: #5e5e5e;
    --page-bg: #e4e4e4;
    --panel: #b9b9b9;
    --card: #c3c4c3;
    --footer-top: #7d7d7d;
    --footer-bottom: #5a5a5a;
    --ink: #1d1d1d;
    --heading: #333333;
    --white: #ffffff;
    --link: #2a4fd8;
    --tick: #e9f2c8;
    --city-dark: #1f2c38;
    --city-mid: #6c8396;
    --city-light: #b9c9d3;
    --hand-dark: #1b2c39;
    --hand-light: #a9c3d2;
  }
  * { box-sizing: border-box; margin: 0; padding: 0; }
  html, body { width: 1200px; height: 1045px; overflow: hidden; }
  body {
    position: relative;
    font-family: "Arimo", Arial, sans-serif;
    background: var(--page-bg);
    color: var(--ink);
  }
  .top-nav {
    position: absolute; left: 0; top: 0; width: 1200px; height: 88px;
    background: linear-gradient(var(--nav-top), var(--nav-bottom));
  }
  .top-nav a {
    position: absolute; top: 37px; color: var(--white);
    font-weight: 700; font-size: 15px; text-decoration: none;
  }
  .top-nav a.is-current { text-shadow: 0 0 6px rgba(255,255,255,.9); }
  .nav-marker { position: absolute; left: 700px; top: 74px; }

  .search-box {
    position: absolute; left: 46px; top: 29px; width: 298px; height: 30px;
    background: linear-gradient(#f4f4f4, #d6d6d6); display: flex; align-items: center;
    font-size: 13px; color: #9c9c9c; padding-left: 25px;
  }
  .search-box svg { position: absolute; right: 8px; top: 7px; }
  .search-box .sep { position: absolute; right: 40px; top: 2px; width: 1px; height: 26px; background: #bcbcbc; }

  .hero-band {
    position: absolute; left: 0; top: 88px; width: 1200px; height: 252px;
    background: linear-gradient(180deg, var(--city-light) 0%, var(--city-mid) 45%, var(--city-dark) 75%, #415566 100%);
  }
  .brand-name {
    position: absolute; left: 56px; top: 150px;
    color: var(--white); font-weight: 700; font-size: 48px; line-height: 52px;
  }
  .call-us {
    position: absolute; left: 796px; top: 244px;
    color: var(--white); font-weight: 700; font-size: 22px;
  }

  .values-panel {
    position: absolute; left: 46px; top: 293px; width: 1107px; height: 327px;
    background: var(--panel);
  }
  .value {
    position: absolute; display: flex; align-items: center; gap: 6px;
    color: var(--white); font-weight: 700; font-size: 30px;
  }
  .handshake-photo {
    position: absolute; left: 550px; top: 334px; width: 560px; height: 246px;
    background: radial-gradient(ellipse at 55% 70%, var(--hand-light), var(--hand-dark) 75%);
  }

  .card { position: absolute; background: var(--card); }
  .card h2 { position: absolute; font-size: 17px; font-weight: 700; color: var(--heading); }
  .about-card { left: 47px; top: 643px; width: 447px; height: 246px; }
  .about-card h2 { left: 29px; top: 27px; }
  .about-card p {
    position: absolute; left: 27px; width: 400px; font-size: 12px; line-height: 14px;
    text-indent: 42px;
  }
  .recent-card { left: 527px; top: 643px; width: 625px; height: 267px; }
  .recent-card h2 { left: 40px; top: 28px; }
  .recent-list { position: absolute; list-style: none; font-size: 12px; line-height: 14px; }
  .recent-list a { color: var(--link); text-decoration: none; }
  .recent-divider { position: absolute; left: 336px; top: 45px; width: 1px; height: 160px; background: #a9a9a9; }

  .footer-band {
    position: absolute; left: 0; top: 860px; width: 1200px; height: 185px;
    background: linear-gradient(var(--footer-top), var(--footer-bottom));
  }
  .services-list { position: absolute; left: 76px; top: 908px; color: #ececec; }
  .services-list h3 { font-size: 13px; font-weight: 700; margin-bottom: 6px; }
  .services-list ul { list-style: none; font-size: 12px; line-height: 20px; }
  .services-list a { color: #e6e6e6; text-decoration: none; }
  .footer-links { position: absolute; left: 369px; top: 944px; font-size: 12px; color: #e6e6e6; }
  .footer-links a { color: #e6e6e6; text-decoration: none; }
  .footer-contact { position: absolute; left: 939px; top: 942px; font-size: 12px; line-height: 17px; color: #ececec; }
</style>
</head>
<body>
  <nav class="top-nav">
    <div class="search-box">Search...
      <span class="sep"></span>
      <svg width="20" height="16" viewBox="0 0 20 16"><path d="M4 1 L16 8 L4 15" fill="none" stroke="#9a9a9a" stroke-width="3"/></svg>
    </div>
    <a href="#" style="left:404px">Home</a>
    <a href="#" style="left:526px">About Us</a>
    <a href="#" class="is-current" style="left:663px">Areas of Law</a>
    <a href="#" style="left:826px">Publications</a>
    <a href="#" style="left:969px">Contacts</a>
    <svg class="nav-marker" width="16" height="14" viewBox="0 0 16 14"><polygon points="0,14 8,6 16,14" fill="#8a8a8a"/></svg>
  </nav>

  <div class="hero-band" role="img" aria-label="Night city skyline with a suspension bridge over the river"></div>
  <div class="brand-name">BRENNICK<br>LAW</div>
  <div class="call-us">Call Us Today: (02) 9046 3270</div>

  <section class="values-panel"></section>
  <div class="value" style="left:100px;top:350px">
    <svg width="46" height="38" viewBox="0 0 46 38"><path d="M4 20 L16 32 L42 4" fill="none" stroke="var(--tick)" stroke-width="6" stroke-linecap="round" stroke-linejoin="round"/></svg>Efficiency</div>
  <div class="value" style="left:161px;top:408px">
    <svg width="46" height="38" viewBox="0 0 46 38"><path d="M4 20 L16 32 L42 4" fill="none" stroke="var(--tick)" stroke-width="6" stroke-linecap="round" stroke-linejoin="round"/></svg>Fulfillment</div>
  <div class="value" style="left:230px;top:462px">
    <svg width="46" height="38" viewBox="0 0 46 38"><path d="M4 20 L16 32 L42 4" fill="none" stroke="var(--tick)" stroke-width="6" stroke-linecap="round" stroke-linejoin="round"/></svg>Integrity</div>
  <div class="value" style="left:299px;top:513px">
    <svg width="46" height="38" viewBox="0 0 46 38"><path d="M4 20 L16 32 L42 4" fill="none" stroke="var(--tick)" stroke-width="6" stroke-linecap="round" stroke-linejoin="round"/></svg>Teamwork</div>
  <div class="handshake-photo" role="img" aria-label="Two business people in suits shaking hands"></div>

  <div class="footer-band"></div>

  <section class="card about-card">
    <h2>ABOUT US</h2>
    <p style="top:74px">Brennick Law is a dynamic commercial law firm in the CBD of Sydney providing services to corporate, small business and private clients. Brennick Law brings together over 30 years of experience in legal practice. The strong focus of the firm is on commercial law and estate planning.</p>
    <p style="top:150px">Brennick Law is committed to providing quality legal services in helping its clients achieve their objectives by providing a proactive understanding of its clients' businesses and creative legal solutions.</p>
  </section>

  <section class="card recent-card">
    <h2>RECENT ADDITIONS</h2>
    <ul class="recent-list" style="left:25px;top:67px;width:305px">
      <li>Commencement of the Succession Act 2006 25.03.08</li>
      <li>Is that will valid? 15.01.08</li>
      <li><a href="#">Labor's proposed changes to IR laws 14.12.07</a></li>
      <li>Should you make your own will? 14.11.07</li>
      <li>Illegal workers 14.08.07</li>
      <li>Employees' liability for misleading or deceptive conduct 14.08.07</li>
    </ul>
    <div class="recent-divider"></div>
    <ul class="recent-list" style="left:354px;top:61px;width:265px">
      <li>Correct use of ACNs and ABNs 14.08.07</li>
      <li>Power of Attorney Infosheet 10.08.07</li>
      <li>Intestate Estates Infosheet 08.08.07</li>
      <li>Estate Planning Infosheet 07.06.07</li>
      <li>Special Disability Trusts Infosheet 18.05.07</li>
      <li>Testamentary Trusts Infosheet 17.05.07</li>
      <li>Appointment of an Enduring Guardian Infosheet 15.05.07</li>
    </ul>
  </section>

  <nav class="services-list">
    <h3>OUR SERVICES</h3>
    <ul>
      <li><a href="#">Commercial Law</a></li>
      <li><a href="#">Estate Planning</a></li>
      <li><a href="#">Wills &amp; Probate</a></li>
      <li><a href="#">Employment Law</a></li>
      <li><a href="#">Business Structures</a></li>
    </ul>
  </nav>

  <div class="footer-links">
    <a href="#">Home</a> | <a href="#">About Us</a> | <a href="#">Area of Law</a> | <a href="#">Our People</a> | <a href="#">Publications</a> | <a href="#">Contact</a>
  </div>
  <div class="footer-contact">
    Telephone (02) 9046 3270<br>
    Facsimile (02) 9046 3281<br>
    Email info@brennicklaw.com.au
  </div>
</body>
</html>
```